Business Card cabinets and cabinets components making company.

the card should be formal and interesting at the same time. The main colors will be black and white.

Font styles to use
Sans Serif

Colors

Designer to choose only greyscale colors for use in the design.

Requirements
Must have
• At least must have the followings:
office phone
cell phone
address
position
name
email
web

```html
<!DOCTYPE html>
<html lang="en">
<head>
<meta charset="utf-8">
<title>Joinwell Business Card</title>
<link href="https://fonts.googleapis.com/css2?family=Roboto:wght@400;500;700&display=swap" rel="stylesheet">
<style>
  :root {
    --backdrop: #3b3b3b;
    --paper: #f1f1f1;
    --ink: #111111;
    --ink-soft: #2a2a2a;
    --stripe-grey: #7a7a7a;
  }
  html, body {
    margin: 0;
    padding: 0;
    width: 799px;
    height: 1200px;
    overflow: hidden;
    background: var(--backdrop);
    font-family: "Roboto", sans-serif;
  }
  .canvas {
    position: relative;
    width: 799px;
    height: 1200px;
  }
  .card {
    position: absolute;
    left: 90px;
    width: 620px;
    height: 354px;
    background: var(--paper);
    overflow: hidden;
    box-shadow: 0 10px 24px rgba(0,0,0,0.45);
  }
  .card-front { top: 130px; }
  .card-back { top: 716px; }

  /* Front */
  .front-brand {
    position: absolute;
    top: 104px;
    left: 0;
    width: 100%;
    text-align: center;
  }
  .wordmark {
    display: inline-flex;
    align-items: center;
    gap: 14px;
    color: var(--ink);
    font-weight: 700;
    letter-spacing: -1px;
  }
  .wordmark-square {
    display: inline-block;
    background: var(--ink);
  }
  .front-brand .wordmark { font-size: 76px; }
  .front-brand .wordmark-square { width: 26px; height: 26px; }
  .front-web {
    position: absolute;
    top: 262px;
    left: 0;
    width: 100%;
    display: flex;
    justify-content: center;
    align-items: center;
    gap: 28px;
    font-size: 16px;
    color: var(--ink-soft);
  }
  .front-web .dash {
    width: 40px;
    height: 3px;
    background: var(--ink);
  }
  .front-edge {
    position: absolute;
    left: 0;
    bottom: 0;
    width: 100%;
    height: 10px;
    background: var(--ink);
  }

  /* Back */
  .identity {
    position: absolute;
    top: 42px;
    left: 40px;
  }
  .person-name {
    margin: 0;
    font-size: 22px;
    font-weight: 700;
    color: var(--ink);
  }
  .person-role {
    margin: 4px 0 0;
    font-size: 13px;
    color: var(--ink-soft);
  }
  .contacts {
    position: absolute;
    top: 214px;
    left: 40px;
    margin: 0;
    padding: 0;
    list-style: none;
    font-size: 15px;
    color: var(--ink-soft);
  }
  .contacts li {
    display: flex;
    align-items: center;
    gap: 12px;
    height: 22px;
  }
  .contacts svg { width: 14px; height: 14px; fill: var(--ink); }
  .contacts .no-icon { padding-left: 26px; }
  .back-brand {
    position: absolute;
    top: 118px;
    right: 48px;
  }
  .back-brand .wordmark { font-size: 50px; gap: 10px; }
  .back-brand .wordmark-square { width: 18px; height: 18px; }
  .address {
    position: absolute;
    top: 238px;
    right: 70px;
    margin: 0;
    font-style: normal;
    text-align: right;
    font-size: 16px;
    line-height: 1.35;
    color: var(--ink-soft);
  }
  .back-band {
    position: absolute;
    left: 0;
    bottom: 0;
    width: 620px;
    height: 50px;
  }
  .back-web {
    position: absolute;
    right: 48px;
    bottom: 10px;
    font-size: 16px;
    color: var(--paper);
  }
</style>
</head>
<body>
<div class="canvas">

  <section class="card card-front" aria-label="Card front">
    <div class="front-brand">
      <span class="wordmark"><span class="wordmark-square"></span>Joinwell</span>
    </div>
    <div class="front-web">
      <span class="dash"></span>
      <span>www.joinwell</span>
      <span class="dash"></span>
    </div>
    <div class="front-edge"></div>
  </section>

  <section class="card card-back" aria-label="Card back">
    <div class="identity">
      <h1 class="person-name">Daniel Hart</h1>
      <p class="person-role">Managing Director</p>
    </div>

    <ul class="contacts">
      <li>
        <svg viewBox="0 0 16 16" aria-hidden="true"><path d="M2 6c0-2 2-3 6-3s6 1 6 3v1h-3V6H5v1H2z M4 8h8l1 6H3z M8 9.5a1.5 1.5 0 1 0 0 3 1.5 1.5 0 0 0 0-3z"/></svg>
        <span>1111-111-1111</span>
      </li>
      <li>
        <svg viewBox="0 0 16 16" aria-hidden="true"><path d="M4 1h8v14H4z M5.5 3v8h5V3z M7 12.5h2v1H7z"/></svg>
        <span>0000-000-0000</span>
      </li>
      <li>
        <svg viewBox="0 0 16 16" aria-hidden="true"><path d="M1 3h14v10H1z M2.5 4.5v.4L8 9l5.5-4.1v-.4z"/></svg>
        <span>daniel@joinwell.com</span>
      </li>
    </ul>

    <div class="back-brand">
      <span class="wordmark"><span class="wordmark-square"></span>Joinwell</span>
    </div>

    <address class="address">
      234 Anywhere St., Any City,<br>
      Any Town, US 123456
    </address>

    <svg class="back-band" viewBox="0 0 620 50" aria-hidden="true">
      <rect x="0" y="40" width="620" height="10" fill="var(--stripe-grey)"/>
      <path d="M300 50 L340 14 Q352 4 368 4 L620 4 L620 50 Z" fill="var(--ink)"/>
    </svg>
    <span class="back-web">www.joinwell.com</span>
  </section>

</div>
</body>
</html>
```